Pemberton Dialworks Business Card Design

Double Sided Business Card Design for a Locksmith company specializing in Safecracking, safe & vault service.

```html
<!DOCTYPE html>
<html lang="en">
<head>
<meta charset="UTF-8">
<title>Pemberton Dialworks Business Card</title>
<link href="https://fonts.googleapis.com/css2?family=Archivo:wght@400;600;800&display=swap" rel="stylesheet">
<style>
  :root {
    --backdrop: #b7b7b7;
    --brand-green: #387a3c;
    --ink-black: #000000;
    --paper-white: #ffffff;
    --dial-tone: #dfe9df;
  }
  html, body {
    margin: 0;
    padding: 0;
    width: 1200px;
    height: 801px;
    overflow: hidden;
    background: var(--backdrop);
    font-family: "Archivo", Arial, sans-serif;
  }
  .card {
    position: absolute;
    top: 274px;
    width: 443px;
    height: 263px;
    overflow: hidden;
    color: var(--paper-white);
  }
  .card--front { left: 153px; background: var(--ink-black); }
  .card--back { left: 625px; background: var(--ink-black); }

  .front-panel {
    position: absolute;
    left: 0; top: 0;
    width: 307px; height: 263px;
    background: var(--brand-green);
  }
  .dial-area {
    position: absolute;
    left: 177px; top: 2px;
    width: 260px; height: 260px;
    border-radius: 50%;
    background: radial-gradient(circle, var(--paper-white) 0%, var(--dial-tone) 100%);
  }
  .holder-name {
    position: absolute;
    left: 18px; top: 34px;
    margin: 0;
    font-size: 17px;
    font-weight: 800;
    letter-spacing: 0.2px;
  }
  .holder-title {
    position: absolute;
    left: 18px; top: 56px;
    margin: 0;
    font-size: 11px;
    font-weight: 400;
    letter-spacing: 0.3px;
  }
  .contact-list {
    position: absolute;
    left: 18px; top: 138px;
    margin: 0; padding: 0;
    list-style: none;
    font-size: 12.5px;
  }
  .contact-list li {
    display: flex;
    align-items: center;
    height: 15.6px;
  }
  .contact-list svg {
    width: 11px; height: 11px;
    margin-right: 5px;
    fill: var(--paper-white);
  }
  .address {
    position: absolute;
    left: 19px; top: 208px;
    margin: 0;
    font-size: 12.5px;
    line-height: 15.6px;
    font-style: normal;
  }

  .brand-mark {
    position: absolute;
    left: 93px; top: 94px;
    width: 76px; height: 76px;
    border-radius: 50%;
    background: var(--brand-green);
  }
  .brand-name {
    position: absolute;
    left: 181px; top: 112px;
    margin: 0;
    font-size: 24px;
    line-height: 23px;
    font-weight: 800;
    letter-spacing: 1px;
    color: var(--paper-white);
  }
  .service-band {
    position: absolute;
    left: 0; top: 211px;
    width: 443px; height: 32px;
    background: var(--brand-green);
    display: flex;
    align-items: center;
    justify-content: center;
    font-size: 11.2px;
    font-weight: 600;
    letter-spacing: 0.2px;
  }
</style>
</head>
<body>
  <section class="card card--front">
    <div class="front-panel"></div>
    <div class="dial-area" role="img" aria-label="Large safe combination dial decoration"></div>
    <h1 class="holder-name">MARCUS HALE</h1>
    <p class="holder-title">MANAGING DIRECTOR</p>
    <ul class="contact-list">
      <li><svg viewBox="0 0 24 24"><path d="M6.6 10.8a15 15 0 0 0 6.6 6.6l2.2-2.2a1 1 0 0 1 1-.25 11.4 11.4 0 0 0 3.6.57 1 1 0 0 1 1 1V20a1 1 0 0 1-1 1A17 17 0 0 1 3 4a1 1 0 0 1 1-1h3.5a1 1 0 0 1 1 1c0 1.25.2 2.45.57 3.6a1 1 0 0 1-.25 1z"/></svg>044-123 456 789</li>
      <li><svg viewBox="0 0 24 24"><path d="M6 2h12v6H6zM3 9h18v8h-3v5H6v-5H3zm5 6v5h8v-5z"/></svg>044-123 456 789</li>
      <li><svg viewBox="0 0 24 24"><path d="M2 5h20v14H2zm2 2v.5l8 5.5 8-5.5V7z"/></svg>info@webname.com</li>
      <li><svg viewBox="0 0 24 24"><path d="M12 2a10 10 0 1 0 0 20 10 10 0 0 0 0-20zm0 2c1 1.4 1.8 3.2 2.1 5H9.9C10.2 7.2 11 5.4 12 4zM4.3 11h3.6c0 .7 0 1.4.1 2H4.3a8 8 0 0 1 0-2zm.9 4h3.1c.3 1.5.9 2.9 1.6 4A8 8 0 0 1 5.2 15zm3.1-6H5.2a8 8 0 0 1 4.7-4c-.7 1.1-1.3 2.5-1.6 4zm3.7 11c-1-1.4-1.7-3.1-2-5h4c-.3 1.9-1 3.6-2 5zm-2.2-7a14 14 0 0 1 0-2h4.4a14 14 0 0 1 0 2zm4.4 6c.7-1.1 1.3-2.5 1.6-4h3.1a8 8 0 0 1-4.7 4zm1.8-6c.1-.6.1-1.3.1-2h3.6a8 8 0 0 1 0 2zm-.2-4c-.3-1.5-.9-2.9-1.6-4a8 8 0 0 1 4.7 4z"/></svg>www.websitename.com</li>
    </ul>
    <address class="address">421, Address line goes here<br>45452,Country Name</address>
  </section>

  <section class="card card--back">
    <div class="brand-mark"></div>
    <p class="brand-name">PEMBERTON<br>DIALWORKS</p>
    <div class="service-band">WE ARE SPECIALIZING IN SAFECRACKING, SAFE &amp; VAULT SERVICE</div>
  </section>
</body>
</html>
```